Business card design for web travel company

Hi
we'd like to receive some proposal for a business card design.
Stayvano is a private travel club, dedicated to all travel lovers, with unique offers for exclusive destinations all around the world. At Stayvano you can find a wide range of offers for resorts, boutique hotels and travel packages at the best guaranteed price available on the market. The convenience of the offer is guaranteed by a private sales model: offers are available for a limited time only and they are personally chosen by Stayvano's qualified team of travel experts.
We offer only exclusive hotels with discounted prices but we are not an outlet or a discount supermarket: the design should reflect our connection with luxury, exclusivity using the same style of our website www.stayvano-example.com.
We want to make sure that when we'll present ourself to our business partner they will feel immediately which is our brand positioning giving them also a sense of an affordable and reliable partner.
In attachment you can also find our brand guidelines (please note that we are NOT USING ANY MORE THE TAG LINE "Five star outlet" mentioned in it).
The info to be inserted are:
Name Surname
Job Title
Tel
Mobile (when needed)
Email
Stayvano S.r.l.
Via Bruno Lesta 27
20131 Milano

```html
<!DOCTYPE html>
<html lang="en">
<head>
<meta charset="utf-8">
<title>Stayvano – Business Card</title>
<link rel="stylesheet" href="https://fonts.googleapis.com/css2?family=Mulish:wght@300;400;700&display=swap">
<style>
  :root {
    --stage: #ece9e5;
    --card-white: #ffffff;
    --ink: #1b1b1b;
    --muted-ink: #555555;
    --gold: #b8a878;
    --card-black: #0d0d0d;
    --stripe-tone: #1e1e1e;
    --light-text: #d6d6d6;
  }
  * { margin: 0; padding: 0; box-sizing: border-box; }
  html, body {
    width: 1200px;
    height: 900px;
    overflow: hidden;
    background: var(--stage);
    font-family: "Mulish", sans-serif;
  }
  .canvas {
    position: relative;
    width: 1200px;
    height: 900px;
  }
  .card {
    position: absolute;
    top: 308px;
    width: 502px;
    height: 286px;
    border-radius: 14px;
    overflow: hidden;
    box-shadow: 0 2px 6px rgba(0,0,0,0.18);
  }
  .card--front {
    left: 75px;
    background: var(--card-white);
    color: var(--ink);
  }
  .card--back {
    left: 626px;
    background: var(--card-black);
  }
  .wordmark {
    position: absolute;
    font-family: "Mulish", sans-serif;
    font-weight: 300;
    letter-spacing: -0.5px;
    line-height: 1;
  }
  .card--front .wordmark {
    right: 32px;
    top: 52px;
    font-size: 54px;
    color: var(--ink);
  }
  .card--back .wordmark {
    right: 34px;
    top: 24px;
    font-size: 46px;
    color: #ffffff;
  }
  .contact {
    position: absolute;
    left: 27px;
    top: 158px;
  }
  .contact__name {
    font-size: 18px;
    font-weight: 700;
    line-height: 22px;
  }
  .contact__surname { color: var(--gold); }
  .contact__title {
    font-size: 12px;
    font-weight: 400;
    line-height: 16px;
    color: var(--muted-ink);
    margin-bottom: 9px;
  }
  .contact__line,
  .company__line {
    font-size: 13px;
    font-weight: 400;
    line-height: 17px;
  }
  .company {
    position: absolute;
    right: 32px;
    bottom: 29px;
    text-align: right;
  }
  .company__name { font-weight: 700; }
  .front-band {
    position: absolute;
    left: 0;
    bottom: 0;
    width: 100%;
    height: 15px;
    background: #000;
  }
  .back-texture {
    position: absolute;
    inset: 0;
    background: linear-gradient(135deg, var(--card-black), var(--stripe-tone) 50%, var(--card-black));
  }
  .website {
    position: absolute;
    left: 30px;
    bottom: 20px;
    font-size: 15px;
    font-weight: 300;
    color: var(--light-text);
    letter-spacing: 0.2px;
  }
</style>
</head>
<body>
  <main class="canvas">
    <section class="card card--front" aria-label="Business card front">
      <div class="wordmark">Stayvano</div>
      <div class="contact">
        <p class="contact__name">Matteo <span class="contact__surname">Gorlani</span></p>
        <p class="contact__title">Partnership Manager</p>
        <p class="contact__line">P : +39 0200 5550</p>
        <p class="contact__line">M : +39 333 555 0192</p>
        <p class="contact__line">E : matteo@stayvano-example.com</p>
      </div>
      <address class="company" style="font-style: normal;">
        <p class="company__line company__name">Stayvano S.r.l.</p>
        <p class="company__line">Via Bruno Lesta 27</p>
        <p class="company__line">20131 Milano</p>
      </address>
      <div class="front-band"></div>
    </section>

    <section class="card card--back" aria-label="Business card back">
      <div class="back-texture" role="img" aria-label="Fine diagonal grey pinstripe texture on black"></div>
      <div class="wordmark">Stayvano</div>
      <p class="website">www.stayvano-example.com</p>
    </section>
  </main>
</body>
</html>
```